Etiketten für Bio-Bienenprodukte
Zielgruppe
Meine Firma (Morgenquell, morgenquell-beispiel.at) mach BIO-Bienenprodukte (Honig, Apitherapie , Schuhpaste aus Bienenwachs, etc).
Zielgruppe: Personen, die regionale & handgemachte Produkte schätzen.
Der Firmensitz liegt auf ca. 900 Meter Seehöhe am Beginn der Alpen (Ostseite).
Aufgabenstellung
Bitte die Musteretikett für Honig beachten (siehe Anhang)

```html
<!DOCTYPE html>
<html lang="de">
<head>
<meta charset="utf-8">
<title>Morgenquell – Honigetiketten</title>
<link href="https://fonts.googleapis.com/css2?family=Oswald:wght@500;700&family=Montserrat:wght@400;600;700&display=swap" rel="stylesheet">
<style>
  :root {
    --page: #ffffff;
    --ink: #111111;
    --paper-white: #ffffff;
    --paper-kraft: #e4d1ab;
    --paper-black: #050505;
    --badge-dark: #1d1d2b;
    --watermark: #ebebeb;
  }
  * { box-sizing: border-box; margin: 0; padding: 0; }
  html, body { width: 1200px; height: 1200px; overflow: hidden; background: var(--page); }
  .sheet { position: relative; width: 1200px; height: 1200px; }

  .label {
    position: absolute;
    border-radius: 50%;
    display: flex; flex-direction: column; align-items: center; justify-content: center;
    text-align: center;
    color: var(--ink);
    font-family: "Montserrat", sans-serif;
    box-shadow: 0 1px 4px rgba(0,0,0,0.12);
    white-space: nowrap;
  }
  .label::after {
    content: ""; position: absolute; inset: 5px;
    border-radius: 50%;
    border: 1.4px solid currentColor;
    border-top-color: transparent;
    transform: rotate(-20deg);
    pointer-events: none;
  }
  .label--white { background: var(--paper-white); }
  .label--kraft { background: var(--paper-kraft); }
  .label--black { background: var(--paper-black); color: #fff; }

  /* back label */
  .label--info { width: 180px; height: 180px; top: 129px; padding-top: 4px; }
  .cert-box {
    width: 94px; border: 1px solid var(--ink); background: #fff; color: var(--ink);
    padding: 3px 4px 2px; margin-bottom: 6px;
  }
  .cert-box__marks { display: flex; justify-content: space-between; align-items: center; }
  .cert-box__eu { width: 44px; height: 29px; background: var(--badge-dark); }
  .cert-box__seal { width: 29px; height: 29px; border-radius: 50%; border: 2px solid var(--ink); }
  .cert-box__code { font-size: 6.2px; line-height: 1.15; text-align: left; margin-top: 2px; white-space: nowrap; }
  .info__title { font-family: "Oswald", sans-serif; font-weight: 500; font-size: 12.5px; line-height: 1.1; margin-bottom: 2px; }
  .info__line { font-size: 6.6px; line-height: 1.05; }
  .info__gap { margin-top: 4px; }
  .info__weight { font-weight: 700; font-size: 16px; line-height: 1.1; margin-top: 2px; }

  /* front label */
  .label--front { width: 150px; height: 150px; }
  .front__mark { width: 26px; height: 26px; border-radius: 50%; border: 1.5px solid currentColor; margin-bottom: 8px; margin-top: 4px; }
  .front__name { font-family: "Oswald", sans-serif; font-weight: 500; font-size: 12.5px; line-height: 1.1; }
  .front__rule { width: 38px; height: 1.5px; background: currentColor; margin: 5px 0 6px; }
  .front__tag { font-size: 6px; font-weight: 600; letter-spacing: 0.9px; }
  .front__variety { font-family: "Oswald", sans-serif; font-weight: 500; font-size: 13px; margin-top: 11px; }

  .col-1 { left: 176px; } .col-2 { left: 505px; } .col-3 { left: 834px; }
  .label--front.col-1 { left: 191px; } .label--front.col-2 { left: 520px; } .label--front.col-3 { left: 849px; }
  .row-first { top: 475px; }
  .row-second { top: 762px; }

  .watermark {
    position: absolute; left: 0; right: 0; top: 985px;
    text-align: center;
    font-family: "Oswald", sans-serif; font-weight: 700;
    font-size: 82px; letter-spacing: 3px;
    color: var(--watermark);
    white-space: nowrap;
  }
</style>
</head>
<body>
<main class="sheet">

  <div class="label label--info label--white col-1">
    <div class="cert-box"><div class="cert-box__marks"><div class="cert-box__eu"></div><div class="cert-box__seal"></div></div><p class="cert-box__code">AT-BIO-999<br>Österreich-Landwirtschaft</p></div>
    <p class="info__title">BIO-Gebirgshonig</p>
    <p class="info__line">Johann Berger, Talweg 12<br>2800 Musterdorf – Am Hang</p>
    <p class="info__line info__gap">Vor Licht und Wärme geschützt lagern</p>
    <p class="info__line info__gap">Mindestens haltbar bis Ende:<br>Tag/Monat/Jahr</p>
    <p class="info__line info__gap">Ursprungsland: Österreich</p>
    <p class="info__weight">250 g</p>
  </div>
  <div class="label label--info label--kraft col-2">
    <div class="cert-box"><div class="cert-box__marks"><div class="cert-box__eu"></div><div class="cert-box__seal"></div></div><p class="cert-box__code">AT-BIO-999<br>Österreich-Landwirtschaft</p></div>
    <p class="info__title">BIO-Gebirgshonig</p>
    <p class="info__line">Johann Berger, Talweg 12<br>2800 Musterdorf – Am Hang</p>
    <p class="info__line info__gap">Vor Licht und Wärme geschützt lagern</p>
    <p class="info__line info__gap">Mindestens haltbar bis Ende:<br>Tag/Monat/Jahr</p>
    <p class="info__line info__gap">Ursprungsland: Österreich</p>
    <p class="info__weight">250 g</p>
  </div>
  <div class="label label--info label--black col-3">
    <div class="cert-box"><div class="cert-box__marks"><div class="cert-box__eu"></div><div class="cert-box__seal"></div></div><p class="cert-box__code">AT-BIO-999<br>Österreich-Landwirtschaft</p></div>
    <p class="info__title">BIO-Gebirgshonig</p>
    <p class="info__line">Johann Berger, Talweg 12<br>2800 Musterdorf – Am Hang</p>
    <p class="info__line info__gap">Vor Licht und Wärme geschützt lagern</p>
    <p class="info__line info__gap">Mindestens haltbar bis Ende:<br>Tag/Monat/Jahr</p>
    <p class="info__line info__gap">Ursprungsland: Österreich</p>
    <p class="info__weight">250 g</p>
  </div>

  <div class="label label--front label--white col-1 row-first"><div class="front__mark"></div><p class="front__name">Morgenquell-beispiel.at</p><div class="front__rule"></div><p class="front__tag">REGIONAL &amp; HANDGEMACHT</p><p class="front__variety">Bruno</p></div>
  <div class="label label--front label--kraft col-2 row-first"><div class="front__mark"></div><p class="front__name">Morgenquell-beispiel.at</p><div class="front__rule"></div><p class="front__tag">REGIONAL &amp; HANDGEMACHT</p><p class="front__variety">Bruno</p></div>
  <div class="label label--front label--black col-3 row-first"><div class="front__mark"></div><p class="front__name">Morgenquell-beispiel.at</p><div class="front__rule"></div><p class="front__tag">REGIONAL &amp; HANDGEMACHT</p><p class="front__variety">Bruno</p></div>

  <div class="label label--front label--white col-1 row-second"><div class="front__mark"></div><p class="front__name">Morgenquell-beispiel.at</p><div class="front__rule"></div><p class="front__tag">REGIONAL &amp; HANDGEMACHT</p><p class="front__variety">Lotte</p></div>
  <div class="label label--front label--kraft col-2 row-second"><div class="front__mark"></div><p class="front__name">Morgenquell-beispiel.at</p><div class="front__rule"></div><p class="front__tag">REGIONAL &amp; HANDGEMACHT</p><p class="front__variety">Lotte</p></div>
  <div class="label label--front label--black col-3 row-second"><div class="front__mark"></div><p class="front__name">Morgenquell-beispiel.at</p><div class="front__rule"></div><p class="front__tag">REGIONAL &amp; HANDGEMACHT</p><p class="front__variety">Lotte</p></div>

  <p class="watermark">Morgenquell-beispiel.at</p>
</main>
</body>
</html>
```